Postcard: Open Sky Circle

Text for front: HOW TO CHANGE THE WORLD IN ONE [note: the word "one" should be underlined] STEPHint: It's up to you...[Note: add arrow or something to indicate "turn over"]Text for back: You're going to spend your entire life with someone you can never get away from. (Guess who?) Wouldn't you rather that person #OpenSkyCircle than judgmental or critical? BE the change you want to see! Visit www.OpenSkyCircle-hub.example for daily Dawn Pebbles and community. PLEASE JOIN US![Note: add logo to left half of back side]Font preference for text: Josefin sans

Target Market(s)

People who would be attracted to Corvane church - teravian perennist message. It's spiritual without being overtly religious, so the target market is probably early 30s and up but ideally won't turn off Millennials (folks under 30). It should attract attention of people who are open-minded and committed to progressive social change, tired of an atmosphere of hate-mongering and divisiveness.

Requirements
Nice to have
• It would be nice to convey a sense of challenge - there is an idea of "dawn pebbles" so something related to fire/sparks is appropriate. This is meant to evoke a deeper, divine love more than a sense of romantic love. This love is more fierce than fluffy! Yet it calls us to be our best selves.
Should not have
• Please avoid excessive pink - just the logo is enough, as this design needs to appeal to men as well as women.

```html
<!DOCTYPE html>
<html lang="en">
<head>
<meta charset="utf-8">
<title>Open Sky Circle — Postcard</title>
<link rel="stylesheet" href="https://fonts.googleapis.com/css2?family=Bebas+Neue&family=Josefin+Sans:wght@300;400&family=Roboto+Slab:wght@400&display=swap">
<style>
  :root {
    --page-bg: #ece9ec;
    --card-grey-light: #e0e0e2;
    --card-grey-dark: #aeaeb1;
    --band-slate: #3b3e46;
    --band-slate-light: #4a4e57;
    --accent-pink: #e8457b;
    --ribbon-pink-dark: #c81f62;
    --ink: #2a2a2a;
    --soft-white: #d9d9dd;
    --white: #ffffff;
  }
  * { box-sizing: border-box; margin: 0; padding: 0; }
  html, body {
    width: 1200px; height: 1200px; overflow: hidden;
    background: var(--page-bg);
  }
  .canvas { position: relative; width: 1200px; height: 1200px; }

  .postcard {
    position: absolute; left: 214px; width: 772px; height: 524px;
    overflow: hidden;
    background: linear-gradient(120deg, var(--card-grey-dark) 0%, var(--card-grey-light) 45%, var(--card-grey-dark) 100%);
    box-shadow: 0 10px 24px rgba(0,0,0,0.25);
  }
  .postcard--front { top: 34px; }
  .postcard--back { top: 634px; }

  .postcard__bands { position: absolute; inset: 0; width: 100%; height: 100%; }

  /* Front */
  .frame { position: absolute; }
  .frame--white {
    left: 110px; top: 91px; width: 505px; height: 340px;
    border: 4px solid rgba(255,255,255,0.9);
    transform: rotate(7deg);
  }
  .frame--pink {
    left: 106px; top: 90px; width: 508px; height: 340px;
    border: 4px solid var(--accent-pink);
  }
  .headline {
    position: absolute; left: 106px; top: 118px; width: 508px;
    text-align: center;
    font-family: 'Bebas Neue', sans-serif; font-weight: 400;
    font-size: 102px; line-height: 84px; letter-spacing: -2px;
    color: var(--ink);
  }
  .headline__line { display: block; }
  .headline__accent { color: var(--accent-pink); }
  .headline__underline { text-decoration: underline; text-decoration-thickness: 4px; text-underline-offset: 6px; }

  .ribbon {
    position: absolute; left: 225px; top: 400px; width: 352px; height: 30px;
    background: linear-gradient(90deg, var(--accent-pink), var(--ribbon-pink-dark));
    transform: rotate(-3deg);
    font-family: 'Roboto Slab', serif; font-size: 16px; letter-spacing: 0.5px;
    color: var(--white); text-align: center; line-height: 30px;
  }
  .hint {
    position: absolute; left: 30px; top: 448px;
    font-family: 'Josefin Sans', sans-serif; font-weight: 400;
    font-size: 32px; line-height: 40px; color: var(--white);
  }

  /* Back */
  .brand {
    position: absolute; left: 30px; top: 40px; width: 236px;
    text-align: center;
  }
  .brand__dot {
    display: block; width: 130px; height: 130px; margin: 0 auto 18px;
    border-radius: 50%; background: var(--accent-pink);
  }
  .brand__name {
    font-family: 'Josefin Sans', sans-serif; font-weight: 400;
    font-size: 26px; color: var(--accent-pink);
  }
  .message {
    position: absolute; left: 306px; top: 30px; width: 462px;
    font-family: 'Josefin Sans', sans-serif; font-weight: 300;
    color: var(--ink);
  }
  .message__text { font-size: 24px; line-height: 34px; }
  .message__question {
    font-size: 42px; line-height: 54px; color: var(--accent-pink);
  }
  .message__url {
    font-size: 28px; line-height: 40px; font-weight: 400; white-space: nowrap;
  }
  .message__url-name { color: var(--accent-pink); }
  .cta {
    position: absolute; left: 30px; top: 428px;
    font-family: 'Bebas Neue', sans-serif; font-size: 84px; letter-spacing: -2px;
    color: var(--soft-white); line-height: 1;
  }
  .cta__light { color: var(--white); }
</style>
</head>
<body>
<main class="canvas">

  <section class="postcard postcard--front" aria-label="Postcard front">
    <svg class="postcard__bands" viewBox="0 0 966 655" preserveAspectRatio="none" aria-hidden="true">
      <polygon points="110,0 966,0 966,262" fill="#3b3e46"/>
      <polygon points="0,330 966,652 966,655 0,655" fill="#3b3e46"/>
      <polygon points="150,12 420,70 160,20" fill="#4a4e57"/>
      <polygon points="40,345 380,440 60,352" fill="#4a4e57"/>
    </svg>
    <div class="frame frame--white"></div>
    <div class="frame frame--pink"></div>
    <h1 class="headline">
      <span class="headline__line">How to change</span>
      <span class="headline__line">the <span class="headline__accent">world</span></span>
      <span class="headline__line">in <span class="headline__underline">one</span> step</span>
    </h1>
    <div class="ribbon">SEE BACK FOR MORE DETAILS!</div>
    <p class="hint">Hint: It's up to you...</p>
  </section>

  <section class="postcard postcard--back" aria-label="Postcard back">
    <svg class="postcard__bands" viewBox="0 0 966 655" preserveAspectRatio="none" aria-hidden="true">
      <polygon points="0,345 966,628 966,655 0,655" fill="#3b3e46"/>
      <polygon points="20,352 420,455 40,360" fill="#4a4e57"/>
    </svg>
    <div class="brand">
      <span class="brand__dot"></span>
      <p class="brand__name">Open Sky Circle</p>
    </div>
    <div class="message">
      <p class="message__text">You're going to spend your entire life with<br>someone you can never get away from.</p>
      <p class="message__question">(GUESS WHO?)</p>
      <p class="message__text">Wouldn't you rather that person<br>#OpenSkyCircle than judgmental or<br>critical? BE the change you want to see!<br>Visit:</p>
      <p class="message__url">www.<span class="message__url-name">OpenSkyCircle</span>-hub.example</p>
      <p class="message__text">for daily Dawn Pebbles and community.</p>
    </div>
    <p class="cta">Please <span class="cta__light">join us!</span></p>
  </section>

</main>
</body>
</html>
```